Child Care Centre needs new roadside billboard / sign*

We have a 2400mm x 1200mm sign that needs to be refreshed. The design is dated and we want to create a new cleaner, more readable roadside signIt needs to be readable from about 100m awayThe text requirements are simple, but we need it to have a warm, family feel.We are located in a small beach side community and we have a lot of bright colours in our centre (a lot of blues and yellows)https://www.maplegrovechildcare.com.au/

Target Market(s)

Parents of young children

Industry/Entity Type

Childcare

Colors
fbed22
0355a3

Requirements
Must have
• Readable from c.100m
• Simple, warm design
Should not have
• Cluttered or overly busy

```html
<!DOCTYPE html>
<html lang="en">
<head>
<meta charset="utf-8">
<title>Maple Grove Early Education – Roadside Sign</title>
<link rel="stylesheet" href="https://fonts.googleapis.com/css2?family=Fredoka:wght@500;600;700&display=swap">
<style>
  :root {
    --ink: #111111;
    --white: #ffffff;
    --sun-yellow: #fbed22;
    --ocean-blue: #0355a3;
    --sign-red: #ed1c24;
    --backdrop: #e9ecef;
    --mascot-yellow: #f5ec3a;
  }
  * { margin: 0; padding: 0; box-sizing: border-box; }
  html, body {
    width: 1200px;
    height: 841px;
    overflow: hidden;
    background: var(--backdrop);
  }
  .canvas {
    position: relative;
    width: 1200px;
    height: 841px;
  }
  .sign {
    position: absolute;
    left: 40px;
    top: 120px;
    width: 1120px;
    height: 600px;
    background: var(--white);
    overflow: hidden;
    font-family: "Fredoka", "Arial Rounded MT Bold", sans-serif;
  }
  .sign-waves {
    position: absolute;
    inset: 0;
    width: 100%;
    height: 100%;
  }
  .mascot {
    position: absolute;
    left: 78px;
    top: 50px;
    width: 165px;
    height: 262px;
    border-radius: 40% 50% 45% 40%;
    background: radial-gradient(circle at 50% 40%, var(--mascot-yellow), #e3d51f);
  }
  .brand {
    position: absolute;
    left: 258px;
    top: 34px;
    line-height: 1;
  }
  .brand-name {
    display: block;
    color: var(--ocean-blue);
    font-weight: 700;
    font-size: 128px;
    letter-spacing: 0;
  }
  .brand-tagline {
    display: block;
    margin-top: 20px;
    margin-left: 72px;
    color: var(--ink);
    font-weight: 500;
    font-size: 96px;
  }
  .services {
    position: absolute;
    left: 45px;
    top: 388px;
    list-style: none;
    color: var(--ink);
    font-weight: 600;
    font-size: 31px;
    line-height: 44px;
  }
  .services .highlight {
    margin-top: 6px;
    color: var(--sign-red);
    font-size: 50px;
    font-weight: 700;
    line-height: 56px;
  }
  .phone-icon {
    position: absolute;
    left: 828px;
    top: 400px;
    width: 98px;
    height: 98px;
  }
  .phone-number {
    position: absolute;
    right: 34px;
    top: 512px;
    color: var(--white);
    font-weight: 700;
    font-size: 76px;
    line-height: 1;
    letter-spacing: 1px;
  }
</style>
</head>
<body>
<main class="canvas">
  <section class="sign">
    <svg class="sign-waves" viewBox="0 0 1120 600" preserveAspectRatio="none" aria-hidden="true">
      <path fill="var(--sun-yellow)" d="M0 340 C90 350 150 385 260 360 C370 335 450 325 560 345 C670 365 740 345 830 330 C930 315 1030 310 1120 300 L1120 600 L0 600 Z"/>
      <path fill="var(--sign-red)" d="M440 600 C500 560 560 550 640 548 C720 546 780 500 830 460 C880 420 920 400 960 395 C1010 390 1040 370 1070 345 C1090 335 1105 333 1120 333 L1120 600 Z"/>
    </svg>

    <div class="mascot" role="img" aria-label="Cartoon seahorse mascot in a graduation cap holding a diploma"></div>

    <h1 class="brand">
      <span class="brand-name">Maple Grove</span>
      <span class="brand-tagline">Early Education</span>
    </h1>

    <ul class="services">
      <li>6 weeks to 6 years (long day care)</li>
      <li>Open 6.30 am – 6.30 pm – 52 weeks a year</li>
      <li>Before and After School Care</li>
      <li class="highlight">Vacation Care</li>
    </ul>

    <svg class="phone-icon" viewBox="0 0 100 100" aria-hidden="true">
      <circle cx="50" cy="50" r="48" fill="var(--sign-red)" stroke="var(--sun-yellow)" stroke-width="2"/>
      <circle cx="50" cy="50" r="33" fill="none" stroke="var(--white)" stroke-width="6"/>
      <path fill="var(--white)" d="M38 33 c3-2 5-1 6 1 l4 7 c1 2 0 4-2 5 l-3 2 c2 5 6 9 11 11 l2-3 c1-2 3-3 5-2 l7 4 c2 1 3 3 1 6 c-3 4-7 5-11 4 c-11-3-20-12-23-23 c-1-4 0-9 3-12 z"/>
    </svg>

    <p class="phone-number">07 4000 2615</p>
  </section>
</main>
</body>
</html>
```